Hi,

I have just started up a business called VOLMIRA in Melbourne. We run fun street art tours around Melbourne's CBD.

I need to create a design for the back side of my business cards. I have designed the front side (simply with my logo) however, I am having trouble designing the reverse side in a professional manner. I have attached pictures of what I have done.

The picture attached titled "VOLMIRA Business Cards Back" has all the information that I require on the back side of my business cards; although displayed in an amateur and simple way. As displayed in the picture, I need: the VOLMIRA logo, the website URL, the booking details (phone - 0468 152 837 & email - bookings@volmira-example.com.au) and the service description ($20, One Hour, Tours Daily, Meet at Halberton St Station). I would also like to use the font in the picture supplied which is "source-sans-pro".

The VOLMIRA tours are for tourists and are relaxed, entertaining and fun! I would like the design to reflect this.

Target Market(s)

Backpackers & University Students

Industry/Entity Type

Business

Requirements
Must have
• The VOLMIRA logo, the website URL, the booking details (phone - 0468 152 837 & email - bookings@volmira-example.com.au) and the service description ($20, One Hour, Tours Daily, Meet at Halberton St Station).

```html
<!DOCTYPE html>
<html lang="en">
<head>
<meta charset="utf-8">
<title>VOLMIRA – Melbourne Street Art Walking Tours</title>
<link rel="stylesheet" href="https://fonts.googleapis.com/css2?family=Arvo&display=swap">
<style>
  :root {
    --paper: #ffffff;
    --ink: #111111;
    --spray-pink: #f4a7a9;
    --spray-pink-soft: #f8c9ca;
    --logo-grey: #9c9c9c;
  }
  * { margin: 0; padding: 0; box-sizing: border-box; }
  html, body {
    width: 1200px;
    height: 676px;
    overflow: hidden;
    background: var(--paper);
  }
  .card {
    position: relative;
    width: 1200px;
    height: 676px;
    background: var(--paper);
    font-family: "Arvo", Georgia, serif;
    color: var(--ink);
    overflow: hidden;
  }
  .spray-band {
    position: absolute;
    left: 0;
    top: 140px;
    width: 1200px;
    height: 390px;
  }
  .brand-mark {
    position: absolute;
    left: 0;
    top: 236px;
    width: 1200px;
    text-align: center;
    font-size: 228px;
    line-height: 1;
    letter-spacing: 6px;
    color: var(--logo-grey);
    font-weight: 400;
  }
  .title {
    position: absolute;
    left: 0;
    top: 34px;
    width: 1200px;
    text-align: center;
    font-size: 55px;
    font-weight: 400;
    line-height: 1.2;
  }
  .title-rule {
    position: absolute;
    left: 169px;
    top: 121px;
    width: 860px;
    height: 3px;
    background: var(--ink);
  }
  .tour-details {
    position: absolute;
    left: 0;
    top: 172px;
    width: 1200px;
    list-style: none;
    text-align: center;
    font-size: 35px;
    line-height: 67.5px;
  }
  .contact {
    position: absolute;
    font-size: 45px;
    line-height: 1;
  }
  .contact-web { left: 34px; top: 546px; }
  .contact-phone { left: 34px; top: 608px; }
  .contact-email { right: 38px; top: 608px; }
</style>
</head>
<body>
  <main class="card">
    <svg class="spray-band" role="img" aria-label="Pink spray-paint band across the card" viewBox="0 0 1200 390" preserveAspectRatio="none">
      <defs>
        <linearGradient id="bandFade" x1="0" y1="0" x2="0" y2="1">
          <stop offset="0" stop-color="#f8c9ca" stop-opacity="0"/>
          <stop offset="0.18" stop-color="#f8c9ca" stop-opacity="0.7"/>
          <stop offset="0.32" stop-color="#f4a7a9"/>
          <stop offset="0.72" stop-color="#f4a7a9"/>
          <stop offset="0.86" stop-color="#f8c9ca" stop-opacity="0.7"/>
          <stop offset="1" stop-color="#f8c9ca" stop-opacity="0"/>
        </linearGradient>
      </defs>
      <rect x="0" y="0" width="1200" height="390" fill="url(#bandFade)"/>
    </svg>

    <div class="brand-mark">VOLMIRA</div>

    <h1 class="title">Melbourne Street Art Walking Tours</h1>
    <div class="title-rule"></div>

    <ul class="tour-details">
      <li>$20 per person</li>
      <li>One hour duration</li>
      <li>Visit a minimum of 3 lanes in Melbourne’s CBD</li>
      <li>Meet under the clocks at Halberton St Station</li>
      <li>Every Monday, Friday &amp; Sunday from 2pm – 3pm</li>
    </ul>

    <p class="contact contact-web">volmira-example.com.au</p>
    <p class="contact contact-phone">0468.152.837</p>
    <p class="contact contact-email">bookings@volmira-example.com.au</p>
  </main>
</body>
</html>
```